Sales Training Power Point Presentation

We are looking for a power point presentation that allows us to turn our training manual into a presentation. I am attaching the training manual here, just to give an idea of what we will be presenting. We want to be able to have graphs for some of that data and be able to move around slides/edit as we see it is needed.

Target Market(s)

new sales employees

Industry/Entity Type

staffing

Colors
0054AA
0677BA
7BADD7
CADEEF
E8F1F8
F0912C
F2A743
F7CA91
FBE8D2
FDF5EE

Requirements
Must have
• graphs

```html
<!DOCTYPE html>
<html lang="en">
<head>
<meta charset="utf-8">
<title>Northvale Group — Sales Training Deck Overview</title>
<link href="https://fonts.googleapis.com/css2?family=Montserrat:wght@400;500;600;700;800&family=Oswald:wght@500;600;700&display=swap" rel="stylesheet">
<style>
:root{
  --navy:#2b3340;
  --navy-soft:#3a4454;
  --orange:#f0782f;
  --orange-soft:#f59a5e;
  --paper:#ffffff;
  --stage:#e8e8ea;
  --ink:#3b3f45;
  --muted:#7a7f86;
  --pill-line:#2b3340;
  --highlight:#fbf3a6;
  --chart-blue:#1f4e8c;
}
*{box-sizing:border-box;margin:0;padding:0}
html,body{width:1200px;height:1108px;overflow:hidden;background:var(--stage)}
body{position:relative;font-family:"Montserrat",sans-serif;color:var(--ink)}
.slide{position:absolute;width:309px;height:194px;background:var(--paper);overflow:hidden;box-shadow:0 10px 8px -6px rgba(0,0,0,.28)}
.c1{left:87px}.c2{left:446px}.c3{left:805px}
.r1{top:83px}.r2{top:324px}.r3{top:572px}.r4{top:816px}
.band{position:absolute;left:0;right:0;bottom:0;height:6px;background:linear-gradient(100deg,var(--orange) 0 66%,var(--navy) 66% 100%)}
.title{position:absolute;left:12px;top:9px;font-size:9.6px;line-height:11px;letter-spacing:.2px}
.title .kicker{display:block;color:var(--orange);font-weight:500}
.title .main{display:block;color:var(--navy);font-weight:600}
.brand{position:absolute;right:8px;top:9px;display:flex;align-items:center;gap:3px}
.brand .dot{width:12px;height:12px;border-radius:50%;background:var(--orange)}
.brand .name{font-weight:700;font-size:5.4px;line-height:5.6px;letter-spacing:.6px;color:var(--navy)}
.brand.light .name{color:#fff}
.body{position:absolute;font-size:3.5px;line-height:4.3px;color:var(--ink)}
.body p{margin-bottom:3.6px;text-align:justify}
.body .accent{color:var(--orange);font-weight:600}
.photo{position:absolute}
/* cover */
.cover .headline{position:absolute;font-family:"Oswald",sans-serif;font-weight:600;color:#fff;font-size:23px;line-height:24px;letter-spacing:-.2px}
.cover .headline .hot{color:var(--orange)}
.cover .tag{position:absolute;color:var(--orange);font-size:5.8px;line-height:6.8px;font-weight:500}
.cover .meta{position:absolute;color:#fff;font-size:4.4px;text-align:right;line-height:8px}
/* pills */
.pillgrid{position:absolute;display:grid;grid-template-columns:1fr 1fr;column-gap:5px;row-gap:3.5px}
.pill{height:11px;border-radius:6px;border:.8px solid var(--pill-line);background:#fff;font-size:4.2px;font-weight:500;display:flex;align-items:center;justify-content:center;color:var(--navy)}
.pill.head{background:var(--navy);color:#fff;border-color:var(--navy)}
.pill.head.hot{background:var(--orange-soft);border-color:var(--orange-soft)}
.dark .pill{border-color:#fff}
.small-label{position:absolute;font-size:3.6px;font-weight:600;color:var(--orange)}
/* thank you */
.thanks{position:absolute;left:13px;top:14px;font-family:"Montserrat",sans-serif;font-weight:800;color:#fff;font-size:26px;line-height:27px}
svg text{font-family:"Montserrat",sans-serif}
</style>
</head>
<body>

<!-- 1 Cover -->
<section class="slide c1 r1 cover">
  <svg class="photo" width="309" height="194" viewBox="0 0 309 194" role="img" aria-label="Photo of a smiling sales team member in a meeting with colleagues">
    <defs><linearGradient id="g1" x1="0" y1="0" x2="1" y2="1"><stop offset="0" stop-color="#d8692a"/><stop offset=".55" stop-color="#9a4a24"/><stop offset="1" stop-color="#3d2a22"/></linearGradient></defs>
    <rect width="309" height="194" fill="url(#g1)"/>
  </svg>
  <svg style="position:absolute;left:0;top:0" width="309" height="194" viewBox="0 0 309 194" aria-hidden="true">
    <polygon points="0,0 135,0 172,194 0,194" fill="var(--navy)"/>
    <polygon points="135,0 140,0 177,194 172,194" fill="var(--orange)"/>
  </svg>
  <div class="brand" style="left:13px;right:auto;top:13px;gap:5px"><span class="dot" style="width:26px;height:26px"></span><span class="name" style="color:#fff;font-size:11px;line-height:11.5px;letter-spacing:1.2px">NORTHVALE<br>GROUP</span></div>
  <div class="headline" style="left:14px;top:88px">POWERING<br><span class="hot">PROGRESSION</span><br>WITH PEOPLE</div>
  <div class="tag" style="left:14px;top:164px">Recruitment solutions for an<br>evolving marketplace.</div>
  <div class="meta" style="right:10px;top:161px">28 July 2023<br>www.northvalegroup.com</div>
</section>

<!-- 2 Intro -->
<section class="slide c2 r1">
  <div class="title"><span class="kicker">SALES TRAINING</span><span class="main">INTRODUCTION</span></div>
  <div class="brand"><span class="dot"></span><span class="name">NORTHVALE<br>GROUP</span></div>
  <div class="body" style="left:13px;top:38px;width:290px">
    <p>Welcome to the Northvale Technology training guide to sales. We are very excited that you have joined our sales team. A career in sales is a worthwhile pursuit and our goal is to better arm you for success. We believe our services are among the best in the industry and plan on continuing this legacy.</p>
    <p>The following pages provide a detailed outline of industry acumen, our Value Proposition, Sales Cycle, Sales Activity, Systems and Tools. These items represent the core of our beliefs in establishing a sales career founded on good principles.</p>
  </div>
  <div class="body" style="left:13px;top:78px;width:160px">
    <p>Selling is defined as the exchange of a product or service for money. It is very important that you keep this principle in mind at all times. There are many varied techniques, systems and processes we use to deliver top-notch services, but all are geared toward one ultimate end: to generate a profit and to make money.</p>
    <p>As you may imagine, the processes and techniques required to excel in sales are more complex than a simple definition implies. Throughout this program we will explore general sales techniques as well as techniques unique to our group.</p>
    <p>The business world continues to evolve around us. A well-trained sales professional sees this evolution as opportunity. This manual is designed to arm you with skills, product knowledge and business focus needed to capitalize on opportunities within the marketplace. The most important tool being product and service knowledge, you must understand our products, services and capabilities to utilize them to a client's advantage.</p>
  </div>
  <svg class="photo" style="left:175px;top:72px" width="125" height="108" viewBox="0 0 125 108" role="img" aria-label="Illustration of business people presenting growth charts and a pie chart">
    <defs><linearGradient id="g2" x1="0" y1="0" x2="0" y2="1"><stop offset="0" stop-color="#e6eef8"/><stop offset="1" stop-color="#c9d9ee"/></linearGradient></defs>
    <rect width="125" height="108" rx="4" fill="url(#g2)"/>
  </svg>
  <div class="band"></div>
</section>

<!-- 3 Intro with photo -->
<section class="slide c3 r1">
  <svg class="photo" width="309" height="194" viewBox="0 0 309 194" role="img" aria-label="Photo of a team working on laptops under a navy tint">
    <defs><linearGradient id="g3" x1="0" y1="0" x2="1" y2="1"><stop offset="0" stop-color="#2e3b52"/><stop offset="1" stop-color="#1c2433"/></linearGradient></defs>
    <rect width="309" height="194" fill="url(#g3)"/>
    <polygon points="0,0 134,0 158,194 0,194" fill="#fff"/>
  </svg>
  <div class="title"><span class="kicker">SALES TRAINING</span><span class="main">INTRODUCTION</span></div>
  <div class="brand light"><span class="dot"></span><span class="name">NORTHVALE<br>GROUP</span></div>
  <div class="body" style="left:12px;top:39px;width:128px">
    <p>The ever-increasing reliance of businesses on computers and technology, much like many other industries, has changed the occupation of sales forever. The availability of information has made our job easier in some ways and leveled the competitive playing field in others, but it has brought the world together in ways never imagined. We will explore new and improved ways of utilizing this technology to the max. Staying ahead of the curve with cutting edge sales tools is our commitment to the sales force.</p>
    <p>Finally, we assist you in creating a map for success, or Business Plan. This map begins with a self-appraisal of your knowledge in the core competencies of the job and ends with a completed game plan delivering you to a desired destination of success. We provide direction in each stage of Business Plan creation and continue through execution. This plan is designed to help you stay the course through what will certainly be an action packed first year on the job.</p>
    <p>The sales profession is a wonderful career. As stated previously, the business environment is ever changing and will provide you with some extremely difficult, yet rewarding, challenges. Being prepared with a great understanding of what we sell and how it helps clients is critical to your success. Welcome aboard! Good Luck!</p>
  </div>
  <div class="band"></div>
</section>

<!-- 4 Industry acumen -->
<section class="slide c1 r2">
  <div class="title"><span class="kicker">INDUSTRY</span><span class="main">ACUMEN</span></div>
  <div class="brand"><span class="dot"></span><span class="name">NORTHVALE<br>GROUP</span></div>
  <div class="body" style="left:13px;top:39px;width:288px">
    <p>For over a century the staffing industry has been called upon to help employers locate employees and vice versa. As time has passed and business has grown more complex, staffing companies have both increased their size and scope. Now the professional services or staffing industry has been touted as one of the fastest growing sectors in the business community. After many years of being almost exclusively linked to low level temp positions and general laborers, recruitment firms can now be found in most of the total job market.</p>
    <p class="accent">The Staffing Industry is made up of the following types of firms:</p>
    <p style="text-align:left">- Contract Services Firm<br>- Direct Placement Firms<br>- Blended Services (Contract / Direct Placement Firms)<br>- Executive Search Firms (Retained Search)</p>
    <p>These staffing organizations may be generalists or can specialize in a specific placement niche such as Office, Industrial, Trades, Legal, Technical, Medical, Home Care and Specialized Executive Search.</p>
    <p>In the USA, the first employment agencies were founded in the late 1800's.</p>
    <p>They include the earliest employment exchanges and engineering agencies, several still operating today.</p>
    <p>While years back, employment agency placement fees were primarily paid for by the applicant, today the client companies pay most employment agency fees.</p>
    <p>The temporary help service industry has the majority of customers.</p>
    <p>In 2018, revenues in staffing were $167 Billion.</p>
    <p>According to the National Staffing Council, over 90% of USA companies utilize temporary help.</p>
  </div>
  <div class="band"></div>
</section>

<!-- 5 Industry acumen chart -->
<section class="slide c2 r2">
  <div class="title"><span class="kicker">INDUSTRY</span><span class="main">ACUMEN</span></div>
  <div class="brand"><span class="dot"></span><span class="name">NORTHVALE<br>GROUP</span></div>
  <svg style="position:absolute;left:9px;top:44px" width="145" height="92" viewBox="0 0 145 92">
    <text x="0" y="3" font-size="3.6" font-weight="700" fill="#222">Staffing and Recruiting Industry Sales Increased 3.9% to $167 Billion in 2018</text>
    <text x="8" y="9" font-size="2.4" font-weight="600" fill="#222">Sales (Billions of U.S. Dollars)—Annual Totals for Staffing and Recruiting Industry</text>
    <g stroke="#ccc" stroke-width=".2">
      <line x1="8" y1="16" x2="140" y2="16"/><line x1="8" y1="30" x2="140" y2="30"/><line x1="8" y1="44" x2="140" y2="44"/><line x1="8" y1="58" x2="140" y2="58"/><line x1="8" y1="72" x2="140" y2="72"/><line x1="8" y1="85" x2="140" y2="85"/>
    </g>
    <g fill="var(--chart-blue)">
      <rect x="10" y="58" width="5.5" height="27"/><rect x="17.8" y="55" width="5.5" height="30"/><rect x="25.6" y="51" width="5.5" height="34"/><rect x="33.4" y="47" width="5.5" height="38"/><rect x="41.2" y="48" width="5.5" height="37"/><rect x="49" y="56" width="5.5" height="29"/><rect x="56.8" y="53" width="5.5" height="32"/><rect x="64.6" y="49" width="5.5" height="36"/><rect x="72.4" y="45" width="5.5" height="40"/><rect x="80.2" y="43" width="5.5" height="42"/><rect x="88" y="40" width="5.5" height="45"/><rect x="95.8" y="38" width="5.5" height="47"/><rect x="103.6" y="36" width="5.5" height="49"/><rect x="111.4" y="34" width="5.5" height="51"/><rect x="119.2" y="32" width="5.5" height="53"/><rect x="127" y="30" width="5.5" height="55"/>
    </g>
    <g fill="var(--orange)">
      <rect x="10" y="54" width="5.5" height="4"/><rect x="17.8" y="51" width="5.5" height="4"/><rect x="25.6" y="46" width="5.5" height="5"/><rect x="33.4" y="42" width="5.5" height="5"/><rect x="41.2" y="43" width="5.5" height="5"/><rect x="49" y="52" width="5.5" height="4"/><rect x="56.8" y="48" width="5.5" height="5"/><rect x="64.6" y="44" width="5.5" height="5"/><rect x="72.4" y="39" width="5.5" height="6"/><rect x="80.2" y="37" width="5.5" height="6"/><rect x="88" y="34" width="5.5" height="6"/><rect x="95.8" y="31" width="5.5" height="7"/><rect x="103.6" y="29" width="5.5" height="7"/><rect x="111.4" y="27" width="5.5" height="7"/><rect x="119.2" y="24" width="5.5" height="8"/><rect x="127" y="22" width="5.5" height="8"/>
    </g>
    <g font-size="2.2" fill="#333"><text x="9" y="89">2003</text><text x="40" y="89">2007</text><text x="71" y="89">2011</text><text x="102" y="89">2015</text><text x="126" y="89">2018</text></g>
  </svg>
  <div class="body" style="left:159px;top:45px;width:141px;height:90px;background:var(--orange);color:#fff;padding:4px 5px;font-size:3.4px;line-height:4px">
    <p>Information Technology represents 15.7% of the market and is the most poised for growth.</p>
    <p>The professional sector (accounting, engineering, information technology and healthcare) increased 9.3% in 2018.</p>
    <p>While several came before, Brightline Staffing, founded in 1946, is widely known as the founder of the modern day temporary help service.</p>
    <p>And while the staffing really developed early on in North America, it is now a global industry.</p>
    <p>There are three and one-half times more temporaries working in Europe than in the USA today.</p>
  </div>
  <div class="body" style="left:12px;top:142px;width:290px">
    <p>As you can see, the staffing industry creates a lucrative and attractive alternative to both employee and employer alike. Offering employees jobs, competitive wages, on the job training and flexible work hours. Meanwhile, offering companies a lean operating model, a flexible workforce, and more.</p>
  </div>
  <div class="band"></div>
</section>

<!-- 6 Product -->
<section class="slide c3 r2">
  <div class="title"><span class="kicker">WHAT IS</span><span class="main">OUR PRODUCT?</span></div>
  <div class="brand"><span class="dot"></span><span class="name">NORTHVALE<br>GROUP</span></div>
  <div class="body" style="left:12px;top:39px;width:288px">
    <p>We provide accounting and finance staffing on a contract and permanent basis.</p>
    <p class="accent" style="margin-bottom:1px">WHO COULD USE OUR PRODUCT?</p>
    <p>We know this is going to sound crazy, but anyone that hires accounting and finance professionals on a contract or permanent basis.</p>
    <p class="accent" style="margin-bottom:1px">WHO HIRES ACCOUNTING PROFESSIONALS?</p>
    <p>Any firm that has an Accounting and/or Finance department.</p>
    <p>So what is staffing? Staffing is a service of sourcing, screening, and retaining professionals to an organization for a fee.</p>
    <p>We provide two types of staffing solutions for our customers. We provide leased employees on a contract basis and regular full time employees for permanent opportunities. The following are the definitions and reasons for both:</p>
    <p>All companies have business objectives they must meet. The amount of capital provided for salaries is the number one expense in most companies in operations today. With that being said, everyone is trying to control the cost of employee resources to obtain profitability, but everyone needs employees in their organizations.</p>
    <p>Fortunately for us, people leave their firm, people get terminated, companies expand, and projects are won. With these determining factors, organizations need to add or replace professionals to their current staff. They can accomplish this in two ways: hiring full time employees or hiring contractors.</p>
    <p>So what is staffing? Staffing is a service of sourcing, screening, and retaining professionals to an organization for a fee.</p>
    <p>We provide two types of staffing solutions for our customers. We provide leased employees on a contract basis and regular full time employees for permanent opportunities. The following are the definitions and reasons for both:</p>
  </div>
  <div class="band"></div>
</section>

<!-- 7 Full time staffing dark -->
<section class="slide c1 r3 dark">
  <svg class="photo" width="309" height="194" viewBox="0 0 309 194" role="img" aria-label="Photo of a team meeting under a dark navy overlay">
    <defs><linearGradient id="g7" x1="0" y1="0" x2="1" y2="1"><stop offset="0" stop-color="#36425a"/><stop offset="1" stop-color="#1e2633"/></linearGradient></defs>
    <rect width="309" height="194" fill="url(#g7)"/>
  </svg>
  <div class="title"><span class="kicker">WHAT IS FULL</span><span class="main" style="color:#fff">TIME STAFFING?</span></div>
  <div class="brand light"><span class="dot"></span><span class="name">NORTHVALE<br>GROUP</span></div>
  <div class="body" style="left:13px;top:35px;width:280px;color:#fff">
    <p>When a staffing firm sources potential candidates that the clients wish to hire directly for full-time employment.</p>
  </div>
  <div class="small-label" style="left:13px;top:44px">FULL TIME STAFFING:</div>
  <div class="body" style="left:13px;top:51px;color:#fff">Definition:&nbsp;&nbsp;The hiring of employees on a full time basis.<br>Reason:&nbsp;&nbsp;&nbsp;&nbsp;&nbsp;&nbsp;Long term employee need for a specific position.</div>
  <div class="small-label" style="left:13px;top:69px">Contract Staffing:</div>
  <div class="pillgrid" style="left:10px;top:83px;width:289px">
    <div class="pill head hot">ADVANTAGES</div><div class="pill head hot">DISADVANTAGES</div>
    <div class="pill">Streamline # of Employees</div><div class="pill">Lower Company Loyalty</div>
    <div class="pill">Hired Expertise</div><div class="pill">Cost for Specific Talent / Rate</div>
    <div class="pill">Reduce Training Costs</div><div class="pill">Short Term Solution</div>
    <div class="pill">Flexibility w/ Employees</div><div class="pill"></div>
    <div class="pill">Overall Cost Saving (Time / $)</div><div class="pill"></div>
  </div>
  <div class="band"></div>
</section>

<!-- 8 Full time staffing light -->
<section class="slide c2 r3">
  <div class="title"><span class="kicker">WHAT IS FULL</span><span class="main">TIME STAFFING?</span></div>
  <div class="brand"><span class="dot"></span><span class="name">NORTHVALE<br>GROUP</span></div>
  <div class="small-label" style="left:14px;top:36px;font-weight:500">FULL TIME STAFFING:</div>
  <div class="pillgrid" style="left:10px;top:44px;width:289px">
    <div class="pill head">ADVANTAGES</div><div class="pill head">DISADVANTAGES</div>
    <div class="pill">Can Create Company Loyalty</div><div class="pill">Long Term Commitment</div>
    <div class="pill">Long Term Staffing Solutions / Team</div><div class="pill">Extensive Hiring Costs / Onboarding</div>
    <div class="pill">Groom in Management</div><div class="pill">Approval Process</div>
    <div class="pill">Cost for Specific Talent</div><div class="pill">Flexibility in Employee Resources</div>
  </div>
  <div class="small-label" style="left:13px;top:124px;font-weight:500">3. Project Based Objectives</div>
  <div class="body" style="left:13px;top:132px;width:288px">
    <p>As corporations try to run more efficiently and increase their bottom line, organizations are streamlining their costs with project based objectives. Project based objectives allow organizations to achieve short and long term goals while reducing fixed costs, thus saving money over time.</p>
    <p>Project based objectives are very prevalent in the A&amp;F industry. There are many reasons why organizations look at A&amp;F for project based solutions. A&amp;F operations are sometimes a non-profit generating arm of the organization. Many companies realize the importance of automation and the use of A&amp;F professionals to run more efficiently, but are reluctant to invest long-term capital.</p>
    <p>Companies can accomplish these objectives by the utilization of project outsourcing and staff augmentation. Here are the differences of the two solutions in its simplest terms.</p>
  </div>
  <div class="band"></div>
</section>

<!-- 9 Sales cycle dashboards -->
<section class="slide c3 r3">
  <div class="title"><span class="kicker">THE SALES</span><span class="main">CYCLE</span></div>
  <div class="brand"><span class="dot"></span><span class="name">NORTHVALE<br>GROUP</span></div>
  <svg style="position:absolute;left:0;top:0" width="309" height="194" viewBox="0 0 309 194">
    <g stroke="#333" stroke-width=".5" fill="#fff">
      <rect x="24" y="44" width="66" height="55"/><rect x="219" y="44" width="66" height="55"/>
      <rect x="24" y="116" width="66" height="51"/><rect x="219" y="116" width="66" height="51"/>
    </g>
    <g font-size="2.6" font-weight="700" fill="#222" text-anchor="middle">
      <text x="57" y="49">SUCCESSFUL PLACEMENTS</text><text x="57" y="52.5">GOAL 80%</text>
      <text x="252" y="49">CANDIDATE ACCURACY</text><text x="252" y="52.5">GOAL 75%</text>
      <text x="57" y="121">INTERVIEW/HIRE</text><text x="57" y="124.5">GOAL 45%</text>
      <text x="252" y="121">FILL RATIO</text><text x="252" y="124.5">GOAL 65%</text>
    </g>
    <!-- pies -->
    <g>
      <ellipse cx="57" cy="78" rx="23" ry="10" fill="#b8591f"/>
      <ellipse cx="57" cy="74" rx="23" ry="10" fill="var(--orange)"/>
      <path d="M57,74 L57,64 A23,10 0 0,0 36,70 Z" fill="var(--navy)"/>
      <ellipse cx="252" cy="78" rx="23" ry="10" fill="#b8591f"/>
      <ellipse cx="252" cy="74" rx="23" ry="10" fill="var(--orange)"/>
      <path d="M252,74 L252,64 A23,10 0 0,1 275,73 Z" fill="var(--chart-blue)"/>
      <ellipse cx="57" cy="147" rx="22" ry="10" fill="#b8591f"/>
      <ellipse cx="57" cy="143" rx="22" ry="10" fill="var(--orange)"/>
      <path d="M57,143 L57,133 A22,10 0 0,1 74,150 Z" fill="var(--chart-blue)"/>
      <ellipse cx="252" cy="147" rx="22" ry="10" fill="#233e6b"/>
      <ellipse cx="252" cy="143" rx="22" ry="10" fill="var(--chart-blue)"/>
      <path d="M252,143 L234,137 A22,10 0 0,1 248,133 Z" fill="var(--orange)"/>
      <path d="M252,143 L248,133 A22,10 0 0,1 256,133 Z" fill="#c9c9c9"/>
    </g>
    <!-- tables -->
    <g font-size="2.5" fill="#222">
      <text x="154" y="38" font-weight="700" text-anchor="middle">SALES</text>
      <text x="109" y="45" font-weight="700">Tasks:</text><text x="131" y="45" font-weight="700">Production:</text><text x="160" y="45" font-weight="700">Goal:</text><text x="178" y="45" font-weight="700">% of Goal:</text>
      <rect x="177" y="60" width="12" height="33" fill="var(--highlight)"/>
      <text x="109" y="50">Fills:</text><text x="109" y="55">Submittals:</text><text x="109" y="60">Interviews:</text><text x="109" y="65">Reqs:</text><text x="109" y="70">Gold:</text><text x="109" y="75">Total Meetings:</text><text x="109" y="80">Total Contacts:</text><text x="109" y="85">New Contacts:</text>
      <text x="138" y="50">152</text><text x="138" y="55">603</text><text x="138" y="60">512</text><text x="138" y="65">343</text><text x="138" y="70">544</text><text x="136" y="75">1,724</text><text x="135" y="80">28,039</text><text x="136" y="85">1,961</text>
      <text x="161" y="50">210</text><text x="161" y="55">650</text><text x="161" y="60">539</text><text x="161" y="65">313</text><text x="161" y="70">480</text><text x="160" y="75">2,542</text><text x="159" y="80">26,177</text><text x="160" y="85">2,866</text>
      <text x="180" y="50">91%</text><text x="180" y="55">93%</text><text x="180" y="60">95%</text><text x="179" y="65">107%</text><text x="180" y="70">83%</text><text x="180" y="75">68%</text><text x="179" y="80">107%</text><text x="180" y="85">69%</text>
      <text x="109" y="96" font-weight="700">% AVG ACTIVITY:</text><text x="178" y="96" font-weight="700">86%</text>
      <text x="154" y="115" font-weight="700" text-anchor="middle">RECRUITING</text>
      <text x="109" y="122" font-weight="700">Tasks:</text><text x="131" y="122" font-weight="700">Production:</text><text x="160" y="122" font-weight="700">Goal:</text><text x="178" y="122" font-weight="700">% of Goal:</text>
      <rect x="177" y="130" width="12" height="30" fill="var(--highlight)"/>
      <text x="109" y="127">Fills:</text><text x="109" y="132">Interviews:</text><text x="109" y="137">Submittals:</text><text x="109" y="142">AI:</text><text x="109" y="147">Matches:</text><text x="109" y="152">Contacts:</text><text x="109" y="157">CN Entered:</text>
      <text x="138" y="127">196</text><text x="138" y="132">508</text><text x="138" y="137">586</text><text x="137" y="142">5,905</text><text x="136" y="147">17,775</text><text x="136" y="152">32,458</text><text x="136" y="157">17,760</text>
      <text x="161" y="127">211</text><text x="161" y="132">545</text><text x="161" y="137">642</text><text x="160" y="142">6,734</text><text x="159" y="147">18,984</text><text x="159" y="152">30,234</text><text x="159" y="157">21,452</text>
      <text x="180" y="127">87%</text><text x="180" y="132">93%</text><text x="180" y="137">91%</text><text x="180" y="142">88%</text><text x="180" y="147">94%</text><text x="179" y="152">107%</text><text x="180" y="157">83%</text>
      <text x="109" y="172" font-weight="700">% AVG ACTIVITY:</text><text x="178" y="172" font-weight="700">93%</text>
    </g>
  </svg>
  <div class="band"></div>
</section>

<!-- 10 Sales cycle phases -->
<section class="slide c1 r4">
  <div class="title"><span class="kicker">THE SALES</span><span class="main">CYCLE</span></div>
  <div class="brand"><span class="dot"></span><span class="name">NORTHVALE<br>GROUP</span></div>
  <div class="body" style="left:12px;top:38px;width:194px">
    <p>What is territory knowledge and why is it important? We answer that question with the end goal in mind. TO MAKE PLACEMENTS! With every end there has to be a beginning. Whether you are launching a new market or maintaining an existing territory, the speed and your ability to know your territory determines where your resource of time must be spent.</p>
    <p>We tend to look at sales territories as puzzles. So how does one start solving a puzzle? We can randomly spread pieces out on a table and start guessing or we can formulate a plan. The first part of the plan may be to take a look at what we are trying to create. Second may be to roughly group the puzzle pieces that look the same. Third may be to place the groups in the general area of the finished picture. Fourth may be to start to identify edge pieces. Fifth may be to put together the border of the puzzle. Sixth may be to start with the area most easily identified. Seventh may be to finish one group at a time. Eighth may be to put all the groups together.</p>
    <p>Sounds easy, right? It sounds much easier in theory than managing a sales territory because it is. You have lay offs, good customers become bad, economic up and down turns, and many other moving parts in a sales territory. We understand the difficulty, but the way you go about understanding your territory should be the same.</p>
  </div>
  <div class="body" style="left:12px;top:157px;line-height:5.6px;font-size:3.6px"><span class="accent" style="font-weight:400">Phase 1:</span> Prospecting / Market Research<br><span class="accent" style="font-weight:400">Phase 2:</span> Account Penetration / Company Research<br><span class="accent" style="font-weight:400">Phase 3:</span> Obtaining Business / Service Delivery<br><span class="accent" style="font-weight:400">Phase 4:</span> Account Retention</div>
  <svg style="position:absolute;left:0;top:0" width="309" height="194" viewBox="0 0 309 194">
    <path d="M231,38 A67,67 0 0,1 278.4,57.6 L256.5,79.5 A36,36 0 0,0 231,69 Z" fill="var(--orange)" stroke="#fff" stroke-width="1.5"/>
    <path d="M278.4,57.6 A67,67 0 0,1 298,105 L267,105 A36,36 0 0,0 256.5,79.5 Z" fill="var(--navy)" stroke="#fff" stroke-width="1.5"/>
    <path d="M298,105 A67,67 0 0,1 278.4,152.4 L256.5,130.5 A36,36 0 0,0 267,105 Z" fill="var(--orange)" stroke="#fff" stroke-width="1.5"/>
    <path d="M278.4,152.4 A67,67 0 0,1 231,172 L231,141 A36,36 0 0,0 256.5,130.5 Z" fill="var(--navy)" stroke="#fff" stroke-width="1.5"/>
    <circle cx="231" cy="105" r="23" fill="var(--navy)"/>
    <circle cx="231" cy="105" r="18" fill="var(--orange)"/>
    <g font-weight="700" font-size="8" fill="#fff"><text x="235" y="53">01</text><text x="269" y="81">02</text><text x="269" y="122">03</text><text x="241" y="155">04</text></g>
    <g font-size="2.4" fill="#fff"><text x="235" y="59">Prospecting</text><text x="269" y="87">Account</text><text x="269" y="90">Penetration</text><text x="269" y="128">Obtaining</text><text x="269" y="131">Business</text><text x="241" y="161">Account</text><text x="241" y="164">Retention</text></g>
  </svg>
  <div class="band"></div>
</section>

<!-- 11 Profits and losses -->
<section class="slide c2 r4">
  <div class="title"><span class="kicker">SALES TRAINING</span><span class="main">INTRODUCTION</span></div>
  <div class="brand"><span class="dot"></span><span class="name">NORTHVALE<br>GROUP</span></div>
  <svg style="position:absolute;left:0;top:0" width="309" height="194" viewBox="0 0 309 194">
    <line x1="30" y1="101" x2="283" y2="101" stroke="var(--navy)" stroke-width=".8"/>
    <circle cx="27" cy="101" r="4.5" fill="var(--navy)"/><path d="M25,101 h4 M27,99 v4" stroke="#fff" stroke-width=".9"/>
    <circle cx="283" cy="101" r="4.5" fill="var(--orange)"/><path d="M281,101 h4" stroke="#fff" stroke-width=".9"/>
    <g fill="var(--navy)">
      <rect x="36" y="82" width="14" height="17" rx="7"/><rect x="61" y="73" width="14" height="26" rx="7"/><rect x="86" y="63" width="14" height="36" rx="7"/><rect x="111" y="53" width="14" height="46" rx="7"/><rect x="136" y="43" width="14" height="56" rx="7"/>
    </g>
    <g fill="var(--orange)">
      <rect x="161" y="103" width="14" height="15" rx="7"/><rect x="186" y="103" width="14" height="24" rx="7"/><rect x="211" y="103" width="14" height="33" rx="7"/><rect x="236" y="103" width="14" height="43" rx="7"/><rect x="261" y="103" width="14" height="53" rx="7"/>
    </g>
    <g fill="#fff"><circle cx="43" cy="90" r="2.6"/><circle cx="68" cy="81" r="2.6"/><circle cx="93" cy="71" r="2.6"/><circle cx="118" cy="61" r="2.6"/><circle cx="143" cy="51" r="2.6"/>
      <circle cx="168" cy="111" r="2.6"/><circle cx="193" cy="120" r="2.6"/><circle cx="218" cy="129" r="2.6"/><circle cx="243" cy="139" r="2.6"/><circle cx="268" cy="149" r="2.6"/></g>
    <g font-size="5.4" font-weight="600" fill="var(--navy)" text-anchor="middle">
      <text x="43" y="78">10%</text><text x="68" y="69">20%</text><text x="93" y="59">30%</text><text x="118" y="49">40%</text><text x="143" y="39">50%</text>
      <text x="168" y="125">10%</text><text x="193" y="134">20%</text><text x="218" y="143">30%</text><text x="243" y="153">40%</text><text x="268" y="163">50%</text>
    </g>
    <rect x="78" y="108" width="30" height="5" rx="2.5" fill="var(--navy)"/><text x="93" y="111.4" font-size="2.4" font-weight="700" fill="#fff" text-anchor="middle">JANUARY - JUNE</text>
    <rect x="203" y="92" width="30" height="5" rx="2.5" fill="var(--orange)"/><text x="218" y="95.4" font-size="2.4" font-weight="700" fill="#fff" text-anchor="middle">JANUARY - JUNE</text>
    <text x="93" y="136" font-size="11" font-weight="700" fill="var(--navy)" text-anchor="middle">Profits</text>
    <g font-size="2.5" fill="var(--muted)" text-anchor="middle"><text x="93" y="141">Quarterly placements grew steadily as the</text><text x="93" y="144">team built strong client relationships and</text><text x="93" y="147">repeat business across every territory.</text></g>
    <text x="218" y="53" font-size="11" font-weight="700" fill="var(--orange)" text-anchor="middle">Losses</text>
    <g font-size="2.5" fill="var(--muted)" text-anchor="middle"><text x="218" y="58">Lost accounts rose when follow-up lagged,</text><text x="218" y="61">showing the cost of missed calls and slow</text><text x="218" y="64">response times with key contacts.</text></g>
  </svg>
  <div class="band"></div>
</section>

<!-- 12 Thank you -->
<section class="slide c3 r4 cover">
  <svg class="photo" width="309" height="194" viewBox="0 0 309 194" role="img" aria-label="Photo of smiling colleagues talking at a table in warm light">
    <defs><linearGradient id="g12" x1="0" y1="0" x2="1" y2="1"><stop offset="0" stop-color="#c95f2a"/><stop offset=".5" stop-color="#8a3f22"/><stop offset="1" stop-color="#3a2620"/></linearGradient></defs>
    <rect width="309" height="194" fill="url(#g12)"/>
  </svg>
  <svg style="position:absolute;left:0;top:0" width="309" height="194" viewBox="0 0 309 194" aria-hidden="true">
    <polygon points="0,0 140,0 167,194 0,194" fill="var(--navy)"/>
    <polygon points="140,0 144,0 171,194 167,194" fill="var(--orange)"/>
  </svg>
  <div class="thanks">THANK<br>YOU!</div>
  <div class="headline" style="left:13px;top:108px;font-size:20px;line-height:20.5px">POWERING<br><span class="hot">PROGRESSION</span><br>WITH PEOPLE</div>
  <div class="tag" style="left:13px;top:171px;font-size:5px;line-height:5.8px">Recruitment solutions for an<br>evolving marketplace.</div>
  <div class="brand" style="right:9px;top:145px;gap:4px"><span class="dot" style="width:24px;height:24px"></span><span class="name" style="color:#fff;font-size:10px;line-height:10.5px;letter-spacing:1px">NORTHVALE<br>GROUP</span></div>
  <div class="meta" style="right:9px;top:175px">www.northvalegroup.com</div>
</section>

</body>
</html>
```